Hexagon Honey Bottle Design, simple and elegant.

Bottle description:
BODY HEIGHT With cap 8.75cm
Without cap 8.6cm
DIAMETER Inner 4.4cm
Outer 5.2cm
Label height only has to be = 6cm height x (3.4X6) length of one hexagonal box is 3.4cm
See through bottle with black cap.
Concept of design:
Elegant, Simple, no pictures of bees, pictures of honeycomb, wooden honey stick, or drooling honey from either is ok. Simple colors. (Designer's discretion)
Wordings:
Hex1
Product of Yemen
Header:
MAROL /TUVI/ (Brand name)
Explanatory below header
Yemen Sidr Honey from The Valley Qarbeen (100% Pure)
(name of honey)
250g
Optional
Hex2
Pure
=
No Additives (not even natural additives)
Hex3
Raw
=
Unheated, Unpasteurized, Unprocessed honey
Hex4
Natural
=
No added color, artificial flavor, or synthetic substance
Hex5
RENOWNED
=
Very well known by honey lovers
(Natural Pure Raw and Renowned) wordings to be on a suitable place on the bottle (maybe on the cap) -
Hex6
Imported By
The Copperfield Trading Pte Ltd
No. 317, Larkspur Grove Road, #09-12
Larkspur Grove Plaza
Singapore 174593
Wordings can be rearranged - its up to the designer's discretion where and how to place them and in which order.-
Designer must be willing to do numerous changes as the design develops

```html
<!DOCTYPE html>
<html lang="en">
<head>
<meta charset="utf-8">
<title>Marol Yemen Sidr Honey – Label &amp; Cap Sticker</title>
<link href="https://fonts.googleapis.com/css2?family=Oswald:wght@300;400;500;600&display=swap" rel="stylesheet">
<style>
  :root{
    --board:#e6e7e8;
    --paper:#ffffff;
    --orange:#f58a2c;
    --brown:#6f635b;
    --ink:#5b514b;
  }
  *{box-sizing:border-box;margin:0;padding:0}
  html,body{width:1200px;height:1200px;overflow:hidden}
  body{background:var(--board);font-family:"Oswald",sans-serif;color:var(--ink);position:relative}
  .board{position:absolute;inset:0;border:1px solid #bbb}

  .cap-sticker{position:absolute;left:790px;top:323px;width:270px;height:270px}
  .cap-sticker text{font-family:"Oswald",sans-serif}

  .wrap-label{position:absolute;left:191px;top:723px;width:894px;height:314px;background:var(--paper)}
  .wrap-label > *{position:absolute}
  .pattern-band{left:9px;top:29px;width:869px;height:43px;background:var(--brown);opacity:.85}
  .claim{top:99px;font-size:11.5px;line-height:14.5px;letter-spacing:.5px;text-transform:uppercase;font-weight:400}
  .claim h3{color:var(--orange);font-weight:500;font-size:11.5px;letter-spacing:.6px;display:inline-block;border-bottom:1.5px solid var(--orange);padding-bottom:1px;margin-bottom:9px}
  .claim-natural{left:21px}
  .claim-renowned{left:21px;top:228px}
  .claim-pure{left:188px}
  .claim-raw{left:540px}
  .claim-imported{left:707px}
  .ornament{width:74px;height:74px;border-radius:50%;background:var(--orange)}
  .ornament-left{left:225px;top:179px}
  .ornament-right{left:568px;top:184px}
  .brand-block{left:342px;width:200px;top:96px;text-align:center}
  .brand-name{color:var(--orange);font-weight:600;font-size:34px;letter-spacing:5px;line-height:38px}
  .brand-sub{font-size:11px;letter-spacing:3px;margin-top:4px;line-height:13px}
  .brand-origin{font-size:7px;letter-spacing:.6px;line-height:10px}
  .bee-mark{left:428px;top:196px;width:28px;height:26px;border-radius:50%;background:var(--orange);opacity:.8}
  .honey-name{left:342px;width:200px;top:246px;text-align:center;color:var(--orange);font-size:13px;letter-spacing:1.5px;font-weight:500}
  .footnote{top:286px;font-size:7.5px;text-transform:uppercase;letter-spacing:.3px}
  .fn-weight{left:307px}
  .fn-origin{left:365px}
  .fn-pure{left:487px}
  .batch-box{left:709px;top:191px;width:150px;height:96px;border:1px solid var(--ink);border-radius:6px}
</style>
</head>
<body>
<div class="board">

  <svg class="cap-sticker" viewBox="0 0 270 270" role="group" aria-label="Cap sticker">
    <defs>
      <path id="arc-top" d="M 33 135 A 102 102 0 0 1 237 135"/>
      <path id="arc-bottom" d="M 18 135 A 117 117 0 0 0 252 135"/>
    </defs>
    <circle cx="135" cy="135" r="135" fill="var(--paper)"/>
    <circle cx="135" cy="135" r="125" fill="none" stroke="var(--orange)" stroke-width="2"/>
    <text font-size="19" fill="var(--ink)" letter-spacing="2" font-weight="400">
      <textPath href="#arc-top" startOffset="50%" text-anchor="middle">NATURAL.PURE.RAW.RENOWNED</textPath>
    </text>
    <text font-size="19" fill="var(--ink)" letter-spacing="2" font-weight="400">
      <textPath href="#arc-bottom" startOffset="50%" text-anchor="middle">PRODUCT OF YEMEN. 250 GM</textPath>
    </text>
    <circle cx="26" cy="128" r="7" fill="var(--orange)" role="img" aria-label="Small sunburst ornament"/>
    <circle cx="244" cy="128" r="7" fill="var(--orange)" role="img" aria-label="Small sunburst ornament"/>
    <text x="135" y="146" text-anchor="middle" font-size="40" font-weight="600" letter-spacing="5" fill="var(--orange)">MAROL</text>
  </svg>

  <section class="wrap-label" aria-label="Wrap-around jar label">
    <div class="pattern-band" role="img" aria-label="Geometric floral lattice pattern band"></div>

    <div class="claim claim-natural">
      <h3>Natural</h3>
      <p>No added color<br>No artificial flavor<br>No synthetic substance</p>
    </div>
    <div class="claim claim-renowned">
      <h3>Renowned</h3>
      <p>Very well known<br>by honey lovers</p>
    </div>
    <div class="claim claim-pure">
      <h3>100% Pure</h3>
      <p>No additives<br>(not even natural additives)</p>
    </div>
    <div class="ornament ornament-left" role="img" aria-label="Orange sunburst flower ornament"></div>

    <div class="brand-block">
      <div class="brand-name">MAROL</div>
      <div class="brand-sub">YEMEN SIDR HONEY</div>
      <div class="brand-origin">FROM THE VALLEY QARBEEN</div>
    </div>
    <div class="bee-mark" role="img" aria-label="Small bee icon"></div>
    <div class="honey-name">NAME OF THE HONEY</div>
    <div class="footnote fn-weight">250 GM</div>
    <div class="footnote fn-origin">Product of Yemen</div>
    <div class="footnote fn-pure">100% Pure</div>

    <div class="claim claim-raw">
      <h3>Raw</h3>
      <p>Unheated<br>Unpasteurized<br>Unprocessed honey</p>
    </div>
    <div class="ornament ornament-right" role="img" aria-label="Orange sunburst flower ornament"></div>

    <div class="claim claim-imported">
      <h3>Imported By</h3>
      <p>The Copperfield Trading Pte Ltd<br>No. 317, Larkspur Grove Road,<br>#09-12 Larkspur Grove Plaza<br>Singapore 174593</p>
    </div>
    <div class="batch-box"></div>
  </section>

</div>
</body>
</html>
```